Moving comapny Postcard mailer Design

I am looking for a 6x9 postcard with real images of our team. I would like to add the same review we currently have , I want the colors of the postcard to be orange and white. I want the team picture to be enlarged with the other pictures to be mimized. I will add example postcards to give rough ideas. My company is called Harlow Moving and the postcards with that name are our current postcards. The additional postcards are from other companies who have better postcards than mine. My goal is for my postcard to be better that theirs.

Target Market(s)

Wealthy people in the 35+ age group

Industry/Entity Type

Moving company

Requirements
Must have
• Beauty

```html
<!DOCTYPE html>
<html lang="en">
<head>
<meta charset="utf-8">
<title>Harlow Moving – Postcard Mailer</title>
<link href="https://fonts.googleapis.com/css2?family=Alfa+Slab+One&family=Kaushan+Script&family=Nunito+Sans:wght@400;600;700;800;900&display=swap" rel="stylesheet">
<style>
  :root{
    --stage:#2b2b2b;
    --orange:#f26a1b;
    --orange-deep:#e5550f;
    --orange-light:#ffa24a;
    --navy:#142f78;
    --blue:#1f52b4;
    --blue-light:#3a74d6;
    --white:#ffffff;
    --ink:#1d1d1d;
  }
  *{box-sizing:border-box;margin:0;padding:0}
  html,body{width:1200px;height:1200px;overflow:hidden;background:var(--stage)}
  body{position:relative;font-family:"Nunito Sans",Arial,sans-serif}

  .postcard{position:absolute;left:218px;width:782px;overflow:hidden;background:var(--white)}
  .postcard--front{top:66px;height:522px;
    background:
      radial-gradient(ellipse 420px 300px at 0% 100%, #fff 35%, rgba(255,255,255,0) 75%),
      linear-gradient(120deg,var(--orange-light) 0%,var(--orange) 45%,var(--orange-deep) 100%);}
  .postcard--back{top:620px;height:519px;
    background:radial-gradient(ellipse 360px 260px at 0% 100%, #e4e4e4 0%, #fff 70%);}
  .abs{position:absolute}

  /* front */
  .front__tagline{left:15px;top:10px;color:var(--white);font-family:"Alfa Slab One",serif;font-size:23px;letter-spacing:.5px;white-space:nowrap}
  .front__tagline em{font-family:"Kaushan Script",cursive;font-style:normal;font-size:24px;margin-left:4px}
  .front__brand{left:12px;top:48px;font-family:"Alfa Slab One",serif;font-size:53px;line-height:50px;color:var(--navy);
    -webkit-text-stroke:2px var(--white);paint-order:stroke fill;text-shadow:3px 3px 0 rgba(0,0,0,.2)}
  .front__phone{left:0;top:160px;width:270px;height:46px;background:var(--white);border:3px solid var(--orange-deep);border-left:none;
    border-radius:0 24px 24px 0;display:flex;align-items:center;justify-content:center;
    font-family:"Alfa Slab One",serif;font-size:25px;color:var(--navy)}
  .front__photo{left:250px;top:38px;width:400px;height:386px;
    background:linear-gradient(180deg,#d8d8d8 0%,#7f8790 40%,#3a3d44 70%,#8d8a80 100%);
    clip-path:polygon(4% 8%,14% 2%,28% 7%,42% 0%,58% 5%,72% 1%,86% 6%,92% 14%,88% 28%,96% 40%,90% 56%,98% 70%,88% 86%,74% 96%,56% 92%,40% 98%,22% 94%,8% 98%,3% 84%,7% 70%,0% 55%,6% 40%,1% 24%)}
  .front__wave{left:0;top:0;width:782px;height:522px}
  .front__logo{left:20px;top:300px;width:230px;display:flex;align-items:center;gap:10px}
  .logo-dot{width:34px;height:34px;border-radius:50%;background:var(--orange);flex:none}
  .logo-name{font-family:"Nunito Sans",Arial,sans-serif;font-weight:900;font-size:27px;color:var(--navy);line-height:1}
  .front__dot{left:20px;top:461px;width:235px;text-align:center;font-size:15px;color:var(--ink)}
  .front__web{left:20px;top:488px;width:235px;text-align:center;font-weight:900;font-size:16px;color:var(--ink);white-space:nowrap}
  .front__web span{color:var(--navy)}
  .stars{left:283px;top:385px;width:252px;height:43px;border-radius:22px;
    background:linear-gradient(180deg,var(--blue-light),var(--navy));border:2px solid var(--white);
    display:flex;align-items:center;justify-content:center}
  .review{left:282px;top:440px;width:450px;font-size:12.2px;line-height:15px;color:var(--ink)}
  .review strong{color:var(--navy);font-weight:800}

  .coupon{left:653px;width:129px;height:120px;background:var(--navy);border:3px solid var(--orange-light);border-right:none;
    border-radius:10px 0 0 10px;color:var(--white);text-align:center;padding-top:10px}
  .coupon__amount{font-weight:900;font-size:22px;line-height:24px}
  .coupon__amount sup{font-size:13px}
  .coupon__terms{font-size:12.5px;line-height:14px;margin-top:2px}
  .coupon__tag{display:block;margin:8px auto 0;width:104px;background:var(--orange);font-size:11px;padding:2px 0}

  /* back */
  .back__hero{left:302px;top:0;width:290px;height:208px;background:linear-gradient(160deg,#cfe2f2 0%,#8ea2b8 45%,#c89b6c 75%,#3e4f7a 100%);
    clip-path:polygon(0 0,88% 0,100% 100%,0 100%)}
  .back__deco{left:0;top:0;width:782px;height:519px}
  .back__title{left:20px;top:10px;font-family:"Alfa Slab One",serif;font-size:38px;line-height:40px;white-space:nowrap;
    color:var(--orange);background:linear-gradient(180deg,var(--orange-light),var(--orange-deep));-webkit-background-clip:text;background-clip:text;-webkit-text-fill-color:transparent;
    filter:drop-shadow(2px 2px 0 rgba(0,0,0,.18))}
  .back__intro{left:20px;top:104px;width:278px;font-size:11.6px;line-height:15px;color:var(--ink)}
  .services-tab{left:0;top:211px;width:137px;height:26px;background:var(--orange-deep);color:var(--white);
    font-weight:800;font-size:15px;padding-left:20px;line-height:26px}
  .services-list{left:131px;top:232px;list-style:none;font-family:"Alfa Slab One",serif;font-size:16px;line-height:19.5px;color:var(--white)}
  .services-list li::before{content:"▸ "}
  .thumb{clip-path:polygon(10% 0,100% 0,90% 100%,0 100%)}
  .thumb--1{left:352px;top:224px;width:226px;height:76px;background:linear-gradient(180deg,#d8dde4,#c09a52 60%,#7c6a55)}
  .thumb--2{left:303px;top:314px;width:220px;height:76px;background:linear-gradient(180deg,#c6ccd3,#8a8f96 55%,#5f6e58)}
  .thumb--3{left:272px;top:407px;width:170px;height:78px;background:linear-gradient(180deg,#9aa8b6,#4e6a86 55%,#7c8a5e)}
  .back__truck{left:443px;top:395px;width:184px;height:118px;background:linear-gradient(180deg,#f4f4f4 0%,#e2e2e2 70%,#5b5b5b 100%);border-radius:6px}
  .back__logo{left:50px;top:380px;display:flex;align-items:center;gap:8px}
  .back__logo .logo-name{font-size:20px}
  .back__logo .logo-dot{width:26px;height:26px}
  .call-pill{left:14px;top:448px;width:208px;height:30px;border-radius:16px;background:linear-gradient(180deg,var(--orange-light),var(--orange-deep));
    border:2px solid var(--white);box-shadow:0 0 0 2px var(--orange-deep);color:var(--white);font-family:"Alfa Slab One",serif;font-size:16px;
    display:flex;align-items:center;justify-content:center}
  .back__phone{left:20px;top:484px;font-family:"Alfa Slab One",serif;font-size:21px;line-height:26px;color:var(--navy)}
</style>
</head>
<body>

<section class="postcard postcard--front" aria-label="Postcard front">
  <div class="abs front__photo" role="img" aria-label="Team photo of the Harlow Moving crew standing in front of a moving truck"></div>
  <svg class="abs front__wave" viewBox="0 0 782 522" aria-hidden="true">
    <path d="M0 522 L0 470 Q220 420 400 408 Q600 396 782 318 L782 522 Z" fill="#ffffff"/>
    <path d="M250 412 Q600 398 782 312" fill="none" stroke="#142f78" stroke-width="7"/>
  </svg>

  <p class="abs front__tagline">ARE YOU MOVING? <em>Let Us Handle Everything!</em></p>
  <h1 class="abs front__brand">HARLOW<br>MOVING</h1>
  <div class="abs front__phone">(865)555-0142</div>

  <div class="abs front__logo"><span class="logo-dot"></span><span class="logo-name">Harlow Moving</span></div>
  <p class="abs front__dot">DOT #4821730</p>
  <p class="abs front__web">WWW.<span>HARLOWMOVER</span>.COM</p>

  <div class="abs coupon" style="top:17px"><div class="coupon__amount"><sup>$</sup>25 OFF</div><div class="coupon__terms">MOVES<br>UNDER 1000</div><span class="coupon__tag">With this card</span></div>
  <div class="abs coupon" style="top:150px"><div class="coupon__amount"><sup>$</sup>50 OFF</div><div class="coupon__terms">MOVES<br>OVER 1000</div><span class="coupon__tag">With this card</span></div>
  <div class="abs coupon" style="top:284px"><div class="coupon__amount"><sup>$</sup>100 OFF</div><div class="coupon__terms">MOVES<br>OVER 3000</div><span class="coupon__tag">With this card</span></div>

  <div class="abs stars" aria-label="Five star rating">
    <svg width="205" height="30" viewBox="0 0 205 30" aria-hidden="true">
      <defs><polygon id="star" points="15,1 19,11 29,11 21,18 24,29 15,22 6,29 9,18 1,11 11,11" fill="#ffffff"/></defs>
      <use href="#star" x="0"/><use href="#star" x="44"/><use href="#star" x="88"/><use href="#star" x="132"/><use href="#star" x="176"/>
    </svg>
  </div>
  <p class="abs review"><strong>The company is incredible!</strong> After working all day, they came to our house and without skipping a beat began efficiently moving our heavy household items. They had a great attitude, very friendly, and clearly enjoyed working with each other! They took extremely good care of my household items. <strong>Thank you for a great experience!</strong></p>
</section>

<section class="postcard postcard--back" aria-label="Postcard back">
  <div class="abs back__hero" role="img" aria-label="Photo of two movers carrying cardboard boxes from a truck"></div>
  <svg class="abs back__deco" viewBox="0 0 782 519" aria-hidden="true">
    <defs>
      <linearGradient id="band" x1="0" y1="0" x2="1" y2="1">
        <stop offset="0" stop-color="#e5550f"/><stop offset=".6" stop-color="#f26a1b"/><stop offset="1" stop-color="#ffa24a"/>
      </linearGradient>
    </defs>
    <polygon points="0,211 610,211 560,300 330,420 0,370" fill="url(#band)"/>
    <polyline points="525,0 612,207 430,519" fill="none" stroke="#f26a1b" stroke-width="4"/>
    <polyline points="545,0 634,207 452,519" fill="none" stroke="#f26a1b" stroke-width="2"/>
  </svg>

  <h2 class="abs back__title">MOVING<br>MADE SIMPLE!</h2>
  <p class="abs back__intro">For over 10 years, our team at Harlow Moving has been providing Eastern Tennessee with unparalleled custom moving experiences. We prioritize safety, timeliness, and communication to ensure our customers are happy and stress-free before, during, and after their move. No matter where you need to go, we're here to help!</p>

  <div class="abs services-tab">SERVICES</div>
  <ul class="abs services-list">
    <li>Local Moving</li>
    <li>Interstate Moving</li>
    <li>Packing &amp; Unpacking</li>
    <li>Hourly Labor</li>
    <li>Junk Removal</li>
  </ul>

  <div class="abs thumb thumb--1" role="img" aria-label="Photo of a moving truck with its loading ramp down"></div>
  <div class="abs thumb thumb--2" role="img" aria-label="Photo of movers carrying furniture outside a house"></div>
  <div class="abs thumb thumb--3" role="img" aria-label="Photo of a mover wrapping furniture in a driveway"></div>
  <div class="abs back__truck" role="img" aria-label="Photo of the white company box truck"></div>

  <div class="abs back__logo"><span class="logo-dot"></span><span class="logo-name">Harlow Moving</span></div>
  <div class="abs call-pill">CALL US TODAY</div>
  <p class="abs back__phone">(865)555-0142</p>
</section>

</body>
</html>
```